Real Estate Cover Template

I am looking for a template design that I can use to post on ZN and TK for my real estate closings and updates. The attachments shows examples...

Company name is Lindmoor Crest Realty and logo is attached.

Seeking:
Just Closed
Under Contract
New Listing
Just Sold
LC Agent

I am looking for something clean that has the company's logo, includes a picture of the subject home, includes sales price and includes our phone # (555-014-3382) and email contact@lindmoorcrest.us.

Examples of competitors are provided for reference.

```html
<!DOCTYPE html>
<html lang="en">
<head>
<meta charset="utf-8">
<title>Lindmoor Crest Realty – Social Post Templates</title>
<link href="https://fonts.googleapis.com/css2?family=Roboto:ital,wght@0,400;0,500;0,700;1,700;1,900&display=swap" rel="stylesheet">
<style>
  :root {
    --brand-blue: #0a4fae;
    --brand-navy: #0b3b80;
    --ink: #1b1b1b;
    --price-grey: #8c8c8c;
    --page: #f7f7f7;
    --tile: #ffffff;
    --corner: #3a3a3a;
    --sky-top: #5d9be0;
    --sky-mid: #b9d6f2;
    --lawn: #6f9a45;
    --drive: #a9aaa8;
  }
  * { box-sizing: border-box; margin: 0; padding: 0; }
  html, body { width: 1200px; height: 1136px; overflow: hidden; background: var(--page); font-family: "Roboto", Arial, sans-serif; color: var(--ink); }
  .post-grid {
    position: absolute; left: 110px; top: 78px;
    display: grid; grid-template-columns: repeat(3, 310px); grid-template-rows: repeat(3, 310px); gap: 25px;
  }
  .post { position: relative; width: 310px; height: 310px; background: var(--tile); overflow: hidden; }

  .home-photo {
    position: absolute; left: 0; right: 0;
    background: linear-gradient(180deg, var(--sky-top) 0%, var(--sky-mid) 42%, #d8c9a6 55%, var(--lawn) 70%, var(--drive) 100%);
  }

  /* brand lockup (name only) */
  .brand { display: flex; align-items: center; gap: 5px; color: var(--brand-blue); font-weight: 700; font-size: 10px; line-height: 1.1; }
  .brand-mark { width: 12px; height: 12px; background: var(--brand-blue); flex: none; }

  /* ===== status header variant ===== */
  .status-head { position: absolute; left: 0; top: 0; width: 310px; height: 78px; }
  .status-head .brand { position: absolute; left: 14px; top: 20px; width: 72px; }
  .status-title { position: absolute; right: 16px; top: 12px; font-weight: 900; font-style: italic; color: var(--brand-blue); letter-spacing: -0.5px; text-align: right; line-height: 1; }
  .status-title.large { font-size: 34px; }
  .status-title.medium { font-size: 27px; top: 16px; }
  .status-title.small { font-size: 22px; top: 18px; }
  .status-price { position: absolute; right: 20px; top: 48px; font-size: 13px; font-style: italic; color: var(--price-grey); }
  .status-rule { position: absolute; left: 0; top: 0; }
  .status-post .home-photo { top: 70px; bottom: 36px; clip-path: polygon(0 16px, 36% 16px, 43% 0, 100% 0, 100% 100%, 0 100%); }

  .contact-strip { position: absolute; left: 0; bottom: 0; width: 310px; height: 36px; display: flex; align-items: center; gap: 8px; padding-left: 10px; font-size: 14px; color: var(--ink); }
  .contact-strip .dot { width: 5px; height: 5px; background: var(--brand-blue); }
  .corner-slash { position: absolute; right: 0; bottom: 0; }

  /* ===== new listing variant ===== */
  .listing-banner { position: absolute; left: 8px; top: 6px; width: 300px; height: 50px; background: var(--brand-blue); display: flex; align-items: baseline; gap: 10px; padding: 10px 14px 0; color: #fff; font-style: italic; }
  .listing-banner .title { font-weight: 900; font-size: 30px; letter-spacing: -0.5px; }
  .listing-banner .price { font-weight: 700; font-size: 14px; }
  .listing-post .home-photo { top: 64px; height: 178px; }
  .listing-foot { position: absolute; left: 0; bottom: 0; width: 310px; height: 68px; display: flex; align-items: center; padding: 0 10px 0 24px; gap: 16px; }
  .listing-foot .brand { width: 66px; }
  .listing-contact .phone { font-size: 20px; letter-spacing: 3.5px; font-weight: 500; }
  .listing-contact .email { font-size: 16px; }

  /* ===== agent variant ===== */
  .agent-post .home-photo { inset: 0; background: linear-gradient(160deg, #e4e7ea 0%, #c8ccd0 45%, #5c6670 75%, #2b3138 100%); }
  .agent-corner { position: absolute; right: 0; top: 0; }
  .agent-post .brand { position: absolute; right: 10px; top: 22px; width: 64px; }
  .agent-card { position: absolute; right: 0; bottom: 0; width: 210px; height: 66px; background: var(--brand-navy); color: #fff; padding: 8px 12px 0 22px; font-size: 14px; line-height: 1.2; }
  .agent-card .name { font-weight: 500; letter-spacing: 1px; }
  .agent-card .phone { letter-spacing: 2.5px; }
  .agent-card .email { font-size: 13px; }
</style>
</head>
<body>
<main class="post-grid">

  <!-- New Listing -->
  <article class="post listing-post">
    <div class="listing-banner"><span class="title">NEW LISTING</span><span class="price">$385.000</span></div>
    <div class="home-photo" role="img" aria-label="Photo of the listed single-storey home with palm trees and lawn"></div>
    <div class="listing-foot">
      <div class="brand"><span class="brand-mark"></span><span>Lindmoor Crest Realty</span></div>
      <div class="listing-contact"><div class="phone">555-014-3382</div><div class="email">contact@lindmoorcrest.us</div></div>
    </div>
  </article>

  <!-- Just Sold -->
  <article class="post status-post">
    <div class="status-head">
      <div class="brand"><span class="brand-mark"></span><span>Lindmoor Crest Realty</span></div>
      <div class="status-title large">JUST SOLD</div>
      <div class="status-price">$385.000</div>
    </div>
    <svg class="status-rule" width="310" height="90" viewBox="0 0 310 90"><polyline points="0,84 112,84 134,68 310,68" fill="none" stroke="var(--brand-blue)" stroke-width="2.5"/></svg>
    <div class="home-photo" role="img" aria-label="Photo of the sold home with double garage and palm tree"></div>
    <div class="contact-strip"><span>555-014-3382</span><span class="dot"></span><span>contact@lindmoorcrest.us</span></div>
    <svg class="corner-slash" width="14" height="36" viewBox="0 0 14 36"><polygon points="8,0 14,0 14,36 0,36" fill="var(--corner)"/></svg>
  </article>

  <!-- Just Closed -->
  <article class="post status-post">
    <div class="status-head">
      <div class="brand"><span class="brand-mark"></span><span>Lindmoor Crest Realty</span></div>
      <div class="status-title medium">JUST CLOSED</div>
      <div class="status-price">$385.000</div>
    </div>
    <svg class="status-rule" width="310" height="90" viewBox="0 0 310 90"><polyline points="0,62 90,62 112,44 310,44" fill="none" stroke="var(--brand-blue)" stroke-width="2.5"/></svg>
    <div class="home-photo" role="img" aria-label="Photo of the closed home with double garage and palm tree"></div>
    <div class="contact-strip"><span>555-014-3382</span><span class="dot"></span><span>contact@lindmoorcrest.us</span></div>
    <svg class="corner-slash" width="14" height="36" viewBox="0 0 14 36"><polygon points="8,0 14,0 14,36 0,36" fill="var(--corner)"/></svg>
  </article>

  <!-- Under Contract -->
  <article class="post status-post">
    <div class="status-head">
      <div class="brand"><span class="brand-mark"></span><span>Lindmoor Crest Realty</span></div>
      <div class="status-title small">UNDER CONTRACT</div>
      <div class="status-price">$385.000</div>
    </div>
    <svg class="status-rule" width="310" height="90" viewBox="0 0 310 90"><polyline points="94,46 310,46" fill="none" stroke="var(--brand-blue)" stroke-width="2"/></svg>
    <div class="home-photo" role="img" aria-label="Photo of the home under contract with palm trees and lawn"></div>
    <div class="contact-strip"><span>555-014-3382</span><span class="dot"></span><span>contact@lindmoorcrest.us</span></div>
    <svg class="corner-slash" width="14" height="36" viewBox="0 0 14 36"><polygon points="8,0 14,0 14,36 0,36" fill="var(--corner)"/></svg>
  </article>

  <!-- New Listing -->
  <article class="post listing-post">
    <div class="listing-banner"><span class="title">NEW LISTING</span><span class="price">$385.000</span></div>
    <div class="home-photo" role="img" aria-label="Photo of the listed single-storey home with palm trees and lawn"></div>
    <div class="listing-foot">
      <div class="brand"><span class="brand-mark"></span><span>Lindmoor Crest Realty</span></div>
      <div class="listing-contact"><div class="phone">555-014-3382</div><div class="email">contact@lindmoorcrest.us</div></div>
    </div>
  </article>

  <!-- Agent -->
  <article class="post agent-post">
    <div class="home-photo" role="img" aria-label="Portrait photo of the agent in a dark blazer"></div>
    <svg class="agent-corner" width="110" height="110" viewBox="0 0 110 110"><polygon points="0,0 110,0 110,110" fill="#fff"/></svg>
    <div class="brand"><span class="brand-mark"></span><span>Lindmoor Crest Realty</span></div>
    <div class="agent-card">
      <div class="name">Aren Voss</div>
      <div class="phone">555-014-3382</div>
      <div class="email">avoss@lindmoorcrest.us</div>
    </div>
  </article>

  <!-- Just Sold -->
  <article class="post status-post">
    <div class="status-head">
      <div class="brand"><span class="brand-mark"></span><span>Lindmoor Crest Realty</span></div>
      <div class="status-title large">JUST SOLD</div>
      <div class="status-price">$385.000</div>
    </div>
    <svg class="status-rule" width="310" height="90" viewBox="0 0 310 90"><polyline points="0,84 112,84 134,68 310,68" fill="none" stroke="var(--brand-blue)" stroke-width="2.5"/></svg>
    <div class="home-photo" role="img" aria-label="Photo of the sold home with double garage and palm tree"></div>
    <div class="contact-strip"><span>555-014-3382</span><span class="dot"></span><span>contact@lindmoorcrest.us</span></div>
    <svg class="corner-slash" width="14" height="36" viewBox="0 0 14 36"><polygon points="8,0 14,0 14,36 0,36" fill="var(--corner)"/></svg>
  </article>

  <!-- Just Closed -->
  <article class="post status-post">
    <div class="status-head">
      <div class="brand"><span class="brand-mark"></span><span>Lindmoor Crest Realty</span></div>
      <div class="status-title medium">JUST CLOSED</div>
      <div class="status-price">$385.000</div>
    </div>
    <svg class="status-rule" width="310" height="90" viewBox="0 0 310 90"><polyline points="0,62 90,62 112,44 310,44" fill="none" stroke="var(--brand-blue)" stroke-width="2.5"/></svg>
    <div class="home-photo" role="img" aria-label="Photo of the closed home with double garage and palm tree"></div>
    <div class="contact-strip"><span>555-014-3382</span><span class="dot"></span><span>contact@lindmoorcrest.us</span></div>
    <svg class="corner-slash" width="14" height="36" viewBox="0 0 14 36"><polygon points="8,0 14,0 14,36 0,36" fill="var(--corner)"/></svg>
  </article>

  <!-- Just Sold -->
  <article class="post status-post">
    <div class="status-head">
      <div class="brand"><span class="brand-mark"></span><span>Lindmoor Crest Realty</span></div>
      <div class="status-title large">JUST SOLD</div>
      <div class="status-price">$385.000</div>
    </div>
    <svg class="status-rule" width="310" height="90" viewBox="0 0 310 90"><polyline points="0,84 112,84 134,68 310,68" fill="none" stroke="var(--brand-blue)" stroke-width="2.5"/></svg>
    <div class="home-photo" role="img" aria-label="Photo of the sold home with double garage and palm tree"></div>
    <div class="contact-strip"><span>555-014-3382</span><span class="dot"></span><span>contact@lindmoorcrest.us</span></div>
    <svg class="corner-slash" width="14" height="36" viewBox="0 0 14 36"><polygon points="8,0 14,0 14,36 0,36" fill="var(--corner)"/></svg>
  </article>

</main>
</body>
</html>
```